4 x Designs Required

Hi There,
I require 4 x different designs to be made for 4 new brands of mine however they can be quite interchangeable. HR Brevlo and Marketing Brevlo can be similar just with a difference in colour. The same goes for the Bulletin brands. This means there are ultimately two designs that need perfecting.

There must be a click here CTA on the banner somewhere. :-)

I require the banners in 728x90 format and 960x90 please.

Please use strap lines on the banners such as:
Essential Whitepapers for HR Professionals
Essential Whitepapers for Marketing Professionals
Your No.1 Whitepaper Resource

The brand names:
HR Brevlo
Marketing Brevlo
HR Gazettor
Marketing Gazettor

Examples attached.

```html
<!DOCTYPE html>
<html lang="en">
<head>
<meta charset="utf-8">
<title>Brevlo Banners</title>
<link rel="stylesheet" href="https://fonts.googleapis.com/css2?family=Questrial&family=Open+Sans:wght@700&display=swap">
<style>
  :root {
    --page-bg: #ffffff;
    --frame-line: #b5b5b5;
    --banner-line: #6e6e6e;
    --ink: #141414;
    --tagline-ink: #2b2b2b;
    --button-top: #ededed;
    --button-bottom: #6a6a6a;
    --button-dark-top: #8a8a8a;
    --button-dark-bottom: #1e1e1e;
    --desk-dark: #3f3a36;
    --desk-mid: #b9a99a;
    --desk-light: #f4ebe2;
    --paper-light: #eeeeec;
    --paper-mid: #d6d5d2;
    --paper-dark: #b8b7b3;
  }
  * { margin: 0; padding: 0; box-sizing: border-box; }
  html, body {
    width: 1200px;
    height: 1200px;
    overflow: hidden;
    background: var(--page-bg);
  }
  .sheet {
    position: relative;
    width: 1200px;
    height: 1200px;
    border: 1px solid var(--frame-line);
  }
  .banner {
    position: absolute;
    height: 106px;
    border: 1px solid var(--banner-line);
    overflow: hidden;
    font-family: "Questrial", sans-serif;
  }
  .banner--hr { left: 172px; top: 473px; width: 858px; }
  .banner--marketing { left: 34px; top: 620px; width: 1132px; }

  .banner__photo {
    position: absolute;
    inset: 0;
  }
  .banner--hr .banner__photo {
    background: linear-gradient(90deg, var(--desk-dark) 0%, var(--desk-mid) 14%, var(--desk-light) 32%, #e9ddd1 55%, var(--desk-light) 75%, #f7efe8 100%);
  }
  .banner--marketing .banner__photo {
    background: linear-gradient(90deg, var(--paper-light) 0%, var(--paper-mid) 35%, var(--paper-light) 48%, var(--paper-dark) 62%, var(--paper-light) 75%, var(--paper-mid) 100%);
  }

  .banner__name {
    position: absolute;
    color: var(--ink);
    white-space: nowrap;
    line-height: 1;
  }
  .banner--hr .banner__name { left: 26px; top: 37px; font-size: 40px; }
  .banner--marketing .banner__name { left: 28px; top: 35px; font-size: 37px; }

  .banner__tagline {
    position: absolute;
    color: var(--tagline-ink);
    white-space: nowrap;
    line-height: 1;
  }
  .banner--hr .banner__tagline { left: 282px; top: 44px; font-size: 20.5px; }
  .banner--marketing .banner__tagline { left: 332px; top: 45px; font-size: 25px; }

  .banner__cta {
    position: absolute;
    border-radius: 8px;
    font-family: "Open Sans", sans-serif;
    font-weight: 700;
    font-size: 18px;
    letter-spacing: 0.5px;
    display: flex;
    align-items: center;
    justify-content: center;
    text-decoration: none;
    box-shadow: 0 2px 3px rgba(0,0,0,0.35);
  }
  .banner--hr .banner__cta {
    left: 720px; top: 31px; width: 109px; height: 45px;
    background: linear-gradient(180deg, var(--button-top), var(--button-bottom));
    color: var(--ink);
  }
  .banner--marketing .banner__cta {
    left: 987px; top: 28px; width: 109px; height: 43px;
    background: linear-gradient(180deg, var(--button-dark-top), var(--button-dark-bottom));
    color: #ffffff;
  }
</style>
</head>
<body>
  <main class="sheet">
    <section class="banner banner--hr">
      <div class="banner__photo" role="img" aria-label="Blurred photo of an office desk with papers and a red pen"></div>
      <div class="banner__name">HR Brevlo</div>
      <p class="banner__tagline">Essential Whitepapers for HR Professionals</p>
      <a class="banner__cta" href="#">SIGN UP</a>
    </section>

    <section class="banner banner--marketing">
      <div class="banner__photo" role="img" aria-label="Soft photo of folded newspaper pages"></div>
      <div class="banner__name">Marketing Brevlo</div>
      <p class="banner__tagline">Essential Whitepapers for Marketing Professionals</p>
      <a class="banner__cta" href="#">SIGN UP</a>
    </section>
  </main>
</body>
</html>
```